Looking for an amazing business card for a thriving DJ business

We need a business card design for a DJ company based in South Florida. The DJ company specializes in weddings, parties, bar mitzvahs, corporate events, proms, and reunions. We are looking for a modern, simple business card design. The card should state DJ Marlow K.
Updates

The name on the card should be DJ Marlow K

Industry/Entity Type

Entertainment Industry

Contact Information for Business Card

DJ Marlow K
512.447.2086
atxdjmarlowk@quellmail.com
https://www.facebook.com/DjMarlowK/
https://www.instagram.com/djmarlow.k/
www.djmarlowk.net

Font styles to use
Serif
Sans Serif

Requirements
Must have
• My business card has to be awesome.
Should not have
• The card has to have personality.

```html
<!DOCTYPE html>
<html lang="en">
<head>
<meta charset="utf-8">
<title>DJ Marlow K – Business Card</title>
<link rel="stylesheet" href="https://fonts.googleapis.com/css2?family=Arimo:wght@400;700&display=swap">
<style>
  :root {
    --stage: #2b2b2b;
    --card-dark: #0e0e0e;
    --card-light: #ffffff;
    --gold: #c39a4c;
    --ink: #3c3f42;
    --rule: #bdbdbd;
  }
  * { box-sizing: border-box; margin: 0; padding: 0; }
  html, body { width: 1200px; height: 1040px; overflow: hidden; }
  body {
    background: var(--stage);
    font-family: "Arimo", Arial, sans-serif;
    position: relative;
  }
  .card {
    position: absolute;
    left: 250px;
    width: 700px;
    height: 400px;
  }
  .card--back {
    top: 70px;
    background: var(--card-dark);
    border-radius: 80px 0 80px 0;
    display: flex;
    align-items: center;
    justify-content: center;
  }
  .card--front {
    top: 570px;
    background: var(--card-light);
    border-radius: 0 80px 0 80px;
  }
  .brand-disc {
    width: 180px;
    height: 180px;
    border-radius: 50%;
    background: var(--card-light);
    border: 3px solid var(--gold);
    display: flex;
    align-items: center;
    justify-content: center;
    text-align: center;
  }
  .brand-name {
    font-family: "Arimo", Arial, sans-serif;
    font-weight: 700;
    font-size: 24px;
    line-height: 1.2;
    color: var(--ink);
  }
  .card--front .brand-disc {
    position: absolute;
    left: 55px;
    top: 100px;
    width: 200px;
    height: 200px;
    border-width: 2px;
  }
  .divider {
    position: absolute;
    left: 305px;
    top: 85px;
    width: 1px;
    height: 230px;
    background: var(--rule);
  }
  .contact {
    position: absolute;
    left: 335px;
    top: 88px;
    color: var(--ink);
  }
  .contact__name {
    color: var(--gold);
    font-weight: 700;
    font-size: 28px;
    letter-spacing: 0.5px;
    margin-bottom: 14px;
  }
  .contact__list { list-style: none; font-size: 19px; line-height: 27px; }
  .contact__list li { display: flex; align-items: center; gap: 10px; white-space: nowrap; }
  .contact__list--social { margin-top: 18px; }
  .icon { width: 18px; height: 18px; flex: none; }
</style>
</head>
<body>

<section class="card card--back" aria-label="Card back">
  <div class="brand-disc">
    <span class="brand-name">Sonora<br>Nights</span>
  </div>
</section>

<section class="card card--front" aria-label="Card front">
  <div class="brand-disc">
    <span class="brand-name">Sonora<br>Nights</span>
  </div>

  <div class="divider"></div>

  <div class="contact">
    <h1 class="contact__name">MARLOW KANE</h1>
    <ul class="contact__list">
      <li>
        <svg class="icon" viewBox="0 0 24 24"><path fill="var(--gold)" d="M6.6 10.8a15.1 15.1 0 0 0 6.6 6.6l2.2-2.2a1 1 0 0 1 1-.25 11.4 11.4 0 0 0 3.6.57 1 1 0 0 1 1 1V20a1 1 0 0 1-1 1A17 17 0 0 1 3 4a1 1 0 0 1 1-1h3.5a1 1 0 0 1 1 1c0 1.25.2 2.45.57 3.57a1 1 0 0 1-.25 1z"/></svg>
        512.447.2086
      </li>
      <li>
        <svg class="icon" viewBox="0 0 24 24"><rect x="2" y="5" width="20" height="14" rx="1" fill="var(--gold)"/><path d="M2.5 6l9.5 7 9.5-7" stroke="#fff" stroke-width="1.6" fill="none"/></svg>
        atxdjmarlowk@quellmail.com
      </li>
      <li>
        <svg class="icon" viewBox="0 0 24 24" fill="none" stroke="var(--gold)" stroke-width="1.8"><circle cx="12" cy="12" r="9"/><ellipse cx="12" cy="12" rx="4" ry="9"/><path d="M3 12h18M5 7h14M5 17h14"/></svg>
        www.djmarlowk.net
      </li>
    </ul>
    <ul class="contact__list contact__list--social">
      <li>
        <svg class="icon" viewBox="0 0 24 24"><circle cx="12" cy="12" r="7" fill="var(--gold)"/></svg>
        www.friendwall.net/DjMarlowK/
      </li>
      <li>
        <svg class="icon" viewBox="0 0 24 24"><rect x="5" y="5" width="14" height="14" rx="2" fill="var(--gold)"/></svg>
        www.photoloop.net/djmarlow.k/
      </li>
    </ul>
  </div>
</section>

</body>
</html>
```